A Global Agro-Commodities Trading Company with HQ in UAE wishes to redesign its Stationery

Creative Brief

Company Profile:
Verlo Crop Holdings is head-quartered in Dubai, United Arab Emirates and specializes in supply chain management of agricultural commodities such as Pulses, Oil Seeds & Edible Oils, Frozen Poultry & Meats, Dairy Products, Animal Feed Raw Materials, Spices, Staples, Dried Fruits, Various Jute Products, Packaging Materials and Special Crops. Verlo Crop’s strategically located network of 24 overseas offices, warehouses, processing and logistics facilities currently exports 54 different food products from 52 countries to over 1000 customers in 82 countries.

Objective:
Design office stationery (Business Cards and Letterheads) such that it provides all the necessary information, gives a corporate feel and is aesthetic. Our current business card template appears cluttered as it has all the information on one side and the Arabic translation on the other. To get rid of the clutter and to make it “easy on the eyes”, we have decided against the Arabic translation and present our global outreach (presence in 24 countries worldwide), in its place.

Key Elements:
- Logo (attached)
- Pantone 285 C (blue) is our official corporate colour. However, we are willing to look at options that have some other subtle colours added to the design to make it look appealing (any other colour added should give a corporate/professional feel)
- We would like to include the following information on the new card:
1. Full Name
2. Designation
3. Company Name
4. Address
5. Company Tel No
6. Fax No
7. Mobile No
8. Email address
9. Website
10. A visual depiction of our presence in 24 countries (a map maybe?) at the back of the card
11. A QR code

We have made an initial start on the redesign in-house using Photoshop, but due to the creative limitations in PS we have decided to seek concepts through Pitch Foundry to help us finalise this project using programs more equipped for this work. For your use and information we have attached the following:
• Current business card template
• Drafts and proposed concepts for the new look
We trust that participants will be able to extend on the drafts with innovative, creative and concise concepts and ideas.
We look forward to your participation and thank you in advance for your creative input

Requirements
Must have
• We would like to include the following information on the new card:
• 1. Full Name
• 2. Designation
• 3. Company Name
• 4. Address
• 5. Company Tel No
• 6. Fax No
• 7. Mobile No
• 8. Email address
• 9. Website
• 10. A visual depiction of our presence in 24 countries (a map maybe?) at the back of the card
• 11. A QR code
Nice to have
• subtle use of an additional color/s (1 - 2) ...Company color Pantone 285C
Should not have
• Enlargement of the logo sun....

```html
<!DOCTYPE html>
<html lang="en">
<head>
<meta charset="utf-8">
<title>Verlo Crop Holdings — Stationery</title>
<link href="https://fonts.googleapis.com/css2?family=Exo+2:wght@600&family=Arimo:wght@400;700&display=swap" rel="stylesheet">
<style>
:root{
  --brand-blue:#1a72bd;
  --brand-blue-light:#cfe2f3;
  --swoosh-grey:#a9abae;
  --paper:#ffffff;
  --backdrop:#eef0f2;
  --ink:#3a3a3a;
  --ink-soft:#666a6e;
}
*{margin:0;padding:0;box-sizing:border-box}
html,body{width:1200px;height:937px;overflow:hidden;background:var(--backdrop)}
body{position:relative;font-family:"Arimo",Arial,sans-serif;color:var(--ink)}
.sheet{position:absolute;background:var(--paper);overflow:hidden}
.wave{position:absolute;left:0;top:0;width:100%}
.brand{position:absolute;display:flex;align-items:center;gap:.3em;font-family:"Exo 2",sans-serif;font-weight:600;color:var(--brand-blue);white-space:nowrap;line-height:1}
.brand-dot{width:.7em;height:.7em;border-radius:50%;background:var(--brand-blue)}

/* letterhead */
.letterhead{left:185px;top:66px;width:386px;height:546px}
.letterhead .wave{height:95px}
.letterhead .brand{left:40px;top:82px;font-size:20px}
.letter{position:absolute;left:36px;top:140px;width:300px;font-size:5.6px;line-height:1.45;color:var(--ink-soft)}
.letter p{margin-bottom:7px}
.letter .gap{margin-bottom:18px}
.letter strong{color:var(--ink)}
.signature{display:block;width:34px;height:16px;background:linear-gradient(90deg,#555,#888);opacity:.35;border-radius:8px;margin:4px 0 6px}
.contact-list{position:absolute;left:36px;top:476px;list-style:none;font-size:5.2px;line-height:1.55;color:var(--ink)}
.contact-list li{display:flex;align-items:center;gap:3px}
.contact-list li::before{content:"";width:4px;height:4px;border-radius:50%;background:var(--brand-blue)}

/* folder */
.folder{left:636px;top:41px;width:460px;height:575px}
.folder .wave{height:120px}
.folder .brand{left:76px;top:270px;font-size:42px}
.rule{position:absolute;border-left:1px dashed var(--ink-soft)}
.folder .rule{left:68px;top:256px;height:72px}

/* cards */
.card{border-radius:9px}
.card-front{left:45px;top:658px;width:177px;height:70px}
.card-front .wave{height:24px}
.card-front .brand{left:10px;top:28px;font-size:10px}
.card-person{position:absolute;left:9px;top:51px;font-size:4.5px;line-height:1.3;color:var(--brand-blue)}
.card-contact{position:absolute;left:122px;top:33px;list-style:none;font-size:3.6px;line-height:1.5;color:var(--ink-soft)}
.card-contact li::before{content:"";display:inline-block;width:3px;height:3px;border-radius:50%;background:var(--brand-blue);margin-right:2px}
.card-back{left:45px;top:785px;width:177px;height:97px}
.card-back .brand{left:16px;top:14px;font-size:10px}
.card-back .rule{left:11px;top:10px;height:18px}
.presence-map{position:absolute;left:74px;top:10px;width:94px;height:60px;border-radius:4px;background:linear-gradient(135deg,var(--brand-blue-light),#9fc4e6)}
.presence-note{position:absolute;left:74px;top:75px;width:94px;font-size:4.4px;text-align:center;color:var(--brand-blue)}
.qr-code{position:absolute;left:16px;top:52px;width:32px;height:32px;border:2px solid var(--brand-blue);background:var(--paper)}

/* envelopes */
.envelope-front{left:265px;top:674px;width:432px;height:206px}
.envelope-front .wave{height:64px}
.envelope-front .brand{left:44px;top:62px;font-size:17px}
.envelope-front .rule{left:34px;top:52px;height:34px}
.envelope-back{left:737px;top:674px;width:419px;height:206px}
.flap{position:absolute;left:0;top:0;width:100%;height:70px;background:var(--brand-blue);border-radius:0 0 42px 42px;display:flex;align-items:center;justify-content:center}
.flap span{font-family:"Exo 2",sans-serif;font-weight:600;font-size:12px;letter-spacing:2.5px;color:var(--paper)}
</style>
</head>
<body>

<svg width="0" height="0" style="position:absolute" aria-hidden="true">
  <defs>
    <symbol id="header-wave" viewBox="0 0 340 80" preserveAspectRatio="none">
      <path fill="var(--swoosh-grey)" d="M0 80 C12 48 50 22 110 22 C150 22 180 36 220 44 C180 30 140 18 104 18 C50 18 14 40 0 62 Z"/>
      <path fill="var(--brand-blue)" d="M0 0 H340 V56 C310 42 276 40 246 46 C200 56 160 26 110 16 C60 8 20 24 0 46 Z"/>
    </symbol>
  </defs>
</svg>

<section class="sheet letterhead" aria-label="Letterhead">
  <svg class="wave" aria-hidden="true"><use href="#header-wave"/></svg>
  <div class="brand"><span class="brand-dot"></span>Verlo Crop</div>
  <div class="letter">
    <p>July 2, 2012</p>
    <p><strong>Dear CH,</strong><br>Palm Tower, 14th St., Dubai UAE</p>
    <p class="gap">Lorem Ipsum is simply dummy text of the printing and typesetting industry. Lorem Ipsum has been the industry's standard dummy text ever since the 1500s, when an unknown printer took a galley of type and scrambled it to make a type specimen book. It has survived not only five centuries, but also the leap into electronic typesetting, remaining essentially unchanged. It was popularised in the 1960s with the release of Letraset sheets containing Lorem Ipsum passages, and more recently with desktop publishing software like Aldus PageMaker including versions of Lorem Ipsum.</p>
    <p class="gap">Lorem Ipsum is simply dummy text of the printing and typesetting industry. Lorem Ipsum has been the industry's standard dummy text ever since the 1500s, when an unknown printer took a galley of type and scrambled it to make.</p>
    <p>Lorem Ipsum is simply dummy text of the printing and typesetting industry. Lorem Ipsum has been the industry's standard dummy text ever since the 1500s, when an unknown printer took a galley of type and scrambled it to make a type specimen book. It has survived not only five centuries, but also the leap into electronic typesetting, remaining essentially unchanged. It was popularised in the 1960s with the release of Letraset sheets containing Lorem Ipsum passages, and more recently with desktop publishing software like Aldus PageMaker including versions of Lorem Ipsum.</p>
    <p>Best Regards,</p>
    <span class="signature" role="img" aria-label="Handwritten signature"></span>
    <p><strong>Daniel Orr</strong><br>Director<br><br>Palm Tower, 14th St., Dubai UAE</p>
  </div>
  <ul class="contact-list">
    <li>Suite 418, Palm Tower, Dubai</li>
    <li>04-310-2200</li>
    <li>04-310-2201</li>
    <li>050-712-4488</li>
    <li>info@verlocrop.ae</li>
    <li>www.verlocrop.ae</li>
  </ul>
</section>

<section class="sheet folder" aria-label="Presentation folder">
  <svg class="wave" aria-hidden="true"><use href="#header-wave"/></svg>
  <span class="rule"></span>
  <div class="brand"><span class="brand-dot"></span>Verlo Crop</div>
</section>

<section class="sheet card card-front" aria-label="Business card front">
  <svg class="wave" aria-hidden="true"><use href="#header-wave"/></svg>
  <div class="brand"><span class="brand-dot"></span>Verlo Crop</div>
  <p class="card-person">Sara Lind<br>Owner / C.E.O</p>
  <ul class="card-contact">
    <li>Suite 418, Palm Tower</li>
    <li>Dubai, UAE</li>
    <li>T 04-310-2200</li>
    <li>F 04-310-2201</li>
    <li>M 050-712-4488</li>
    <li>info@verlocrop.ae</li>
    <li>www.verlocrop.ae</li>
  </ul>
</section>

<section class="sheet card card-back" aria-label="Business card back">
  <span class="rule"></span>
  <div class="brand"><span class="brand-dot"></span>Verlo Crop</div>
  <div class="qr-code" role="img" aria-label="QR code linking to the company website"></div>
  <div class="presence-map" role="img" aria-label="World map marking offices in 24 countries"></div>
  <p class="presence-note">Offices in 24 countries</p>
</section>

<section class="sheet envelope-front" aria-label="Envelope front">
  <svg class="wave" aria-hidden="true"><use href="#header-wave"/></svg>
  <span class="rule"></span>
  <div class="brand"><span class="brand-dot"></span>Verlo Crop</div>
</section>

<section class="sheet envelope-back" aria-label="Envelope back">
  <div class="flap"><span>www.verlocrop.ae</span></div>
</section>

</body>
</html>
```